label design for supplement product veltracor

label design
Need to design 3 label for 3 products.
PRODUCTS NAME are respectively:
1. Postpartum Hair Regrowth - Barcode: 284061735218
2. Postpartum Bone Support - barcode: 284061482397
3. Postpartum Daily Best  (is multi Vitamin - Barcode: 284061650724
Attachment:
1. Label template as attachments.
- Non-GMO needs to take away
- Hair Effect need to take away
2. Logo  “VeltraCor” as attachment
3. Bottle use as attachment
4. I also attached some simply picture of mom and baby that i like
Detail information:
1. These 3 products belong to the same series called “Meadow Nest”
2. distributed by: VeltraCor. Fremont, CA 94517, U.S.A
3. For the the Blank space in the template
Product one: Postpartum Hair regrowth
• Supports healthy hair growth and texture*
* Nourishes and repairs hair follicles*
• May keep hair from turning gray*
• Provides glossy, youthful hair*
• Leads to healthy hair growth in postpartum mom
* * Promotes blood flow to the scalp*
Product two: postpartum bone support
Vitamin K2 + Resveratrol is a dietary supplement that supports:
• Bone structure, density and integrity*
• Proper bone remodeling and mineralization* • Cardiovascular Function*
• Brain Function*
• Free-Radical Fighters*
We want to show and simple drawing of a mom or a mom and a baby. So that we delivery a very clear message to the customer we are target to postpartum mom .
we Like simple, clean design.

Target Market(s)
new mom
Look and feel
Each slider illustrates characteristics of the customer's brand and the style your logo design should communicate.

```html
<!DOCTYPE html>
<html lang="en">
<head>
<meta charset="utf-8">
<title>VeltraCor Meadow Nest Postpartum Hair Growth Label</title>
<link rel="stylesheet" href="https://fonts.googleapis.com/css2?family=Comfortaa:wght@700&family=Montserrat:wght@500;600;800&display=swap">
<style>
  :root {
    --page: #f4f4f4;
    --label-black: #0b0b0b;
    --label-sheen: #4a4a4a;
    --title-white: #e6e6e6;
    --text-white: #efefef;
    --brand-red: #a31218;
    --rule-red: #b3141b;
    --gold-light: #f3df9a;
    --gold-mid: #c79b4a;
    --gold-dark: #6f4d1c;
    --ornament-red: #b8262c;
  }
  * { margin: 0; padding: 0; box-sizing: border-box; }
  html, body { width: 1200px; height: 1200px; overflow: hidden; background: var(--page); }
  .canvas { position: relative; width: 1200px; height: 1200px; }

  .label {
    position: absolute; left: 100px; top: 45px; width: 1000px; height: 1110px;
    background: linear-gradient(100deg, var(--label-black) 0%, #1c1c1c 30%, var(--label-sheen) 62%, #222 82%, var(--label-black) 100%);
    font-family: "Montserrat", sans-serif; color: var(--text-white);
  }
  .centered { position: absolute; left: 0; width: 100%; text-align: center; }

  .brand-name {
    top: 78px; font-family: "Montserrat", sans-serif; font-weight: 800;
    font-size: 60px; color: var(--brand-red);
  }
  .series-title {
    font-family: "Comfortaa", sans-serif; font-weight: 700; color: var(--title-white);
    line-height: 1;
  }
  .series-title.line-one { top: 190px; font-size: 150px; }
  .series-title.line-two { top: 352px; font-size: 150px; }

  .product-tag {
    position: absolute; left: 266px; top: 527px; width: 478px; height: 64px;
    background: linear-gradient(90deg, var(--gold-light), var(--gold-mid) 40%, var(--gold-dark) 70%, var(--gold-light));
    color: #111; font-weight: 800; font-size: 56px; line-height: 64px; text-align: center;
    letter-spacing: 1px;
  }
  .product-name { top: 598px; font-weight: 800; font-size: 64px; color: var(--brand-red); letter-spacing: 1px; }
  .product-claim { top: 676px; font-weight: 500; font-size: 23px; }
  .red-rule { position: absolute; height: 3px; background: var(--rule-red); }
  .red-rule.upper { left: 266px; width: 478px; top: 714px; }
  .red-rule.lower { left: 338px; width: 336px; top: 1015px; }

  .benefit-list { top: 742px; list-style: none; font-weight: 500; font-size: 21px; line-height: 37.5px; }

  .capsule-count { position: absolute; left: 415px; top: 900px; width: 180px; height: 110px; overflow: visible; }
  .supplement-type { top: 1036px; font-weight: 500; font-size: 21px; letter-spacing: 5px; }

  .ornament { position: absolute; border-radius: 30px;
    background: linear-gradient(180deg, var(--gold-light), var(--ornament-red) 50%, var(--gold-mid)); }
  .ornament.left-top { left: 48px; top: 140px; width: 60px; height: 200px; }
  .ornament.right-top { left: 855px; top: 50px; width: 55px; height: 112px; }
  .ornament.left-middle { left: 130px; top: 583px; width: 75px; height: 285px; }
  .ornament.right-middle { left: 763px; top: 806px; width: 80px; height: 97px; }
  .ornament.right-bottom { left: 905px; top: 790px; width: 48px; height: 258px; }
  .ornament.left-bottom { left: 81px; top: 945px; width: 64px; height: 97px; }
</style>
</head>
<body>
<div class="canvas">
  <section class="label">
    <div class="centered brand-name">VeltraCor</div>

    <div class="ornament left-top" role="img" aria-label="Gold oval and red and gold leaf ornament"></div>
    <div class="ornament right-top" role="img" aria-label="Red and gold leaf sprig ornament"></div>
    <div class="ornament left-middle" role="img" aria-label="Leaf chain ornament with gold circle"></div>
    <div class="ornament right-middle" role="img" aria-label="Red and gold leaf sprig ornament"></div>
    <div class="ornament right-bottom" role="img" aria-label="Leaf and triangle ornament column"></div>
    <div class="ornament left-bottom" role="img" aria-label="Red and gold leaf sprig ornament"></div>

    <h1 class="centered series-title line-one">Meadow</h1>
    <div class="centered series-title line-two">Nest</div>

    <div class="product-tag">POSTPARTUM</div>
    <h2 class="centered product-name">HAIR GROWTH</h2>
    <p class="centered product-claim">Supports Healthy Hair Growth And Texture</p>
    <div class="red-rule upper"></div>

    <ul class="centered benefit-list">
      <li>Nourishes And Repairs Hair Follicles*</li>
      <li>May Keep Hair From Turning Gray*</li>
      <li>Provides Glossy, Youthful Hair*</li>
      <li>Promotes Blood Flow To The Scalp*</li>
    </ul>

    <svg class="capsule-count" viewBox="0 0 180 110" aria-label="60 vegetarian capsules">
      <defs><path id="capsule-arc" d="M33.6,98.5 A60,60 0 1 1 146.4,98.5"/></defs>
      <text font-family="Montserrat, sans-serif" font-size="13" font-weight="600" fill="#efefef" letter-spacing="1">
        <textPath href="#capsule-arc" startOffset="50%" text-anchor="middle">VEGETARIAN CAPSULES</textPath>
      </text>
      <text x="90" y="98" text-anchor="middle" font-family="Montserrat, sans-serif" font-size="52" font-weight="800" fill="#a31218">60</text>
    </svg>
    <div class="red-rule lower"></div>
    <p class="centered supplement-type">DIETARY SUPPLEMENT</p>
  </section>
</div>
</body>
</html>
```